Business Card Design needed for logo design project

This project is linked to Logo: brand identity for modern furniture design studio..

Our company needs a Business Card Design. Please refer to our original project in the link above.

Industry/Entity Type

Business

```html
<!DOCTYPE html>
<html lang="en">
<head>
<meta charset="utf-8">
<title>novari business card</title>
<link rel="stylesheet" href="https://fonts.googleapis.com/css2?family=Jost:wght@400;500;600&display=swap">
<style>
  :root {
    --page-bg: #ffffff;
    --card-paper: #f1f1f1;
    --ink: #2f2f2f;
    --ink-soft: #3a3a3a;
    --rule: #c9c9c9;
    --band: #333333;
  }
  html, body {
    margin: 0;
    padding: 0;
    width: 1200px;
    height: 465px;
    overflow: hidden;
    background: var(--page-bg);
    font-family: "Jost", sans-serif;
    color: var(--ink);
  }
  .canvas {
    position: relative;
    width: 1200px;
    height: 465px;
  }
  .card {
    position: absolute;
    width: 414px;
    height: 238px;
    border-radius: 4px;
    overflow: hidden;
  }
  .card-paper {
    position: absolute;
    inset: 0;
    background: linear-gradient(180deg, #f4f4f4 0%, var(--card-paper) 100%);
  }
  .card--front { left: 174px; top: 105px; }
  .card--back  { left: 611px; top: 119px; }

  .front-band {
    position: absolute;
    left: 0; top: 0;
    width: 100%;
    height: 11px;
    background: var(--band);
  }
  .front-wordmark {
    position: absolute;
    left: 0; right: 0;
    top: 72px;
    text-align: center;
    font-weight: 400;
    font-size: 84px;
    line-height: 1;
    letter-spacing: 2px;
    color: var(--ink);
  }

  .back-tab {
    position: absolute;
    left: 0; top: 95px;
    width: 10px;
    height: 45px;
    background: var(--band);
  }
  .back-wordmark {
    position: absolute;
    left: 46px;
    top: 98px;
    font-weight: 400;
    font-size: 44px;
    line-height: 1;
    letter-spacing: 1px;
    color: var(--ink);
  }
  .back-divider {
    position: absolute;
    left: 202px;
    top: 50px;
    width: 1px;
    height: 131px;
    background: var(--rule);
  }
  .contact {
    position: absolute;
    left: 228px;
    top: 52px;
    font-size: 12px;
    line-height: 15px;
    color: var(--ink-soft);
  }
  .contact-name {
    margin: 0 0 6px;
    font-size: 17px;
    font-weight: 600;
    line-height: 20px;
    color: var(--ink);
  }
  .contact-address,
  .contact-phone,
  .contact-email,
  .contact-web { margin: 0; }
  .contact-phone { margin-top: 8px; }
  .contact-email { margin-top: 5px; }
  .contact-web { margin-top: 3px; font-weight: 600; color: var(--ink); }
</style>
</head>
<body>
  <main class="canvas">
    <section class="card card--front" aria-label="Business card front">
      <div class="card-paper" role="img" aria-label="White wood grain paper texture"></div>
      <div class="front-band"></div>
      <div class="front-wordmark">novari</div>
    </section>

    <section class="card card--back" aria-label="Business card back">
      <div class="card-paper" role="img" aria-label="White wood grain paper texture"></div>
      <div class="back-tab"></div>
      <div class="back-wordmark">novari</div>
      <div class="back-divider"></div>
      <div class="contact">
        <p class="contact-name">Mara Lind</p>
        <p class="contact-address">Studio Nord<br>48 Kiln Lane,<br>Leeds, England.</p>
        <p class="contact-phone">+12 (0)456 789 210</p>
        <p class="contact-email">Info@novari.com</p>
        <p class="contact-web">www.novari.com</p>
      </div>
    </section>
  </main>
</body>
</html>
```